Career development coaching - school lever to adults, needs a business card

Tandem Lark - An independent Career Advice business that provides 1-2-1 advice,for career development, entrepreneurial support and workshops needs a business card. Our clients of all ages (school leaver to adults looking for a career move) and universities and colleges. We would like the card to be double-sided with a modern, professional look. Looking for something professional yet very creative and original. Want a standard size business card that inspires a second look because it stands out from the rest.

One side of the card to have a design incorporating the logo with Tandem Lark name with the strap line “Helping you find your future” and space for the company website

Other side of the card to the logo/Tandem Lark name and the usual contact information:
Individual Name
Job Title (for example, Director)
Phone number
Email address
Company website address

Facebook, LinkedIn and Twitter links will need to go somewhere (back or front!)

The design will be used for 3 individuals so should be editable so that we can update as needed/as we grow.

Attached is the company logo/colours to be incorporated.

Target Market(s)

1-2-1 advice,for career development, entrepreneurial support and workshops needs a business card. Our clients of all ages (school leaver to adults looking for a career move) and universities and colleges.

Industry/Entity Type

Consulting

Contact Information for Business Card

Individual Name
Phone number
Email address
Company website address

Font styles to use
Sans Serif

Colors
0255a3
3176b5
faa54b
f78f20
85acd3
cfdeed

Requirements
Must have
• use the Tandem Lark Logo in some way - using the colours and the blue/orange palette
• For the logo - hope this makes sense to someone or if they direclty relate to the logo image attached!
• For the Orange:- Pantone 1585 C
• In CMYK : C3 M71 Y100 K0
• For the Blue:- 100% Pantone 7469 C
• In CMYK : C100 M62 Y27 K7
• Please feel free to contact me with any questions for more info
Nice to have
• happy to see any creative designs
Should not have
• Nothing too traditional,

```html
<!DOCTYPE html>
<html lang="en">
<head>
<meta charset="utf-8">
<title>Tandem Lark — Business Card</title>
<link rel="stylesheet" href="https://fonts.googleapis.com/css2?family=Questrial&family=Arimo:wght@400;700&display=swap">
<style>
  :root {
    --backdrop: #9b9b9b;
    --paper: #f1f1f3;
    --brand-blue: #175a84;
    --brand-orange: #cc5f2c;
    --ink-grey: #555a60;
    --white: #f4f4f4;
  }
  * { margin: 0; padding: 0; box-sizing: border-box; }
  html, body {
    width: 1105px;
    height: 1200px;
    overflow: hidden;
    background: var(--backdrop);
  }
  .canvas {
    position: relative;
    width: 1105px;
    height: 1200px;
  }
  .card {
    position: absolute;
    left: 182px;
    width: 746px;
    height: 425px;
    overflow: hidden;
  }
  .card--front { top: 119px; background: var(--paper); }
  .card--back  { top: 637px; background: var(--brand-orange); }

  .front__mark {
    position: absolute;
    left: 315px;
    top: 36px;
    width: 124px;
    height: 124px;
    border-radius: 50%;
    background: var(--brand-orange);
  }
  .front__wordmark {
    position: absolute;
    left: 0; right: 0;
    top: 180px;
    text-align: center;
    font-family: "Questrial", sans-serif;
    font-size: 32px;
    letter-spacing: 1px;
    text-transform: uppercase;
    color: var(--brand-blue);
  }
  .front__tagline {
    position: absolute;
    left: 0; right: 0;
    top: 216px;
    text-align: center;
    font-family: "Arimo", sans-serif;
    font-size: 15px;
    text-transform: uppercase;
    color: var(--ink-grey);
  }
  .person__name {
    position: absolute;
    left: 0; right: 0;
    top: 262px;
    text-align: center;
    font-family: "Arimo", sans-serif;
    font-size: 27px;
    letter-spacing: 0.5px;
    text-transform: uppercase;
    color: var(--brand-blue);
  }
  .person__title {
    position: absolute;
    left: 0; right: 0;
    top: 296px;
    text-align: center;
    font-family: "Arimo", sans-serif;
    font-size: 18px;
    text-transform: uppercase;
    color: var(--brand-orange);
  }
  .contact {
    position: absolute;
    left: 0; right: 0;
    top: 333px;
    text-align: center;
    font-family: "Arimo", sans-serif;
    font-size: 18px;
    color: var(--ink-grey);
  }
  .contact__label { font-weight: 700; color: var(--brand-blue); }
  .contact__web {
    position: absolute;
    left: 0; right: 0;
    top: 358px;
    text-align: center;
    font-family: "Arimo", sans-serif;
    font-weight: 700;
    font-size: 18px;
    letter-spacing: 1.5px;
    text-transform: uppercase;
    color: var(--brand-blue);
  }
  .front__bar {
    position: absolute;
    left: 0; bottom: 0;
    width: 100%;
    height: 12px;
    display: flex;
  }
  .front__bar-blue { width: 371px; background: var(--brand-blue); }
  .front__bar-gap { width: 4px; background: var(--white); }
  .front__bar-orange { flex: 1; background: var(--brand-orange); }

  .back__wordmark {
    position: absolute;
    left: 0; right: 0;
    top: 150px;
    text-align: center;
    font-family: "Questrial", sans-serif;
    font-size: 62px;
    letter-spacing: 2px;
    text-transform: uppercase;
    color: var(--white);
  }
  .back__social {
    position: absolute;
    left: 0; right: 0;
    top: 340px;
    display: flex;
    justify-content: center;
    gap: 10px;
  }
  .social-dot {
    width: 43px;
    height: 43px;
    border-radius: 50%;
    background: var(--white);
  }
</style>
</head>
<body>
<main class="canvas">
  <section class="card card--front">
    <div class="front__mark"></div>
    <h1 class="front__wordmark">Tandem Lark</h1>
    <p class="front__tagline">Helping you find your future</p>
    <h2 class="person__name">Maya Rensford</h2>
    <p class="person__title">President</p>
    <p class="contact"><span class="contact__label">P :</span> 555 0142 7788 <span class="contact__label">E :</span> maya@tandemlark.com</p>
    <p class="contact__web">www.tandemlark.com</p>
    <div class="front__bar">
      <span class="front__bar-blue"></span>
      <span class="front__bar-gap"></span>
      <span class="front__bar-orange"></span>
    </div>
  </section>

  <section class="card card--back">
    <p class="back__wordmark">Tandem Lark</p>
    <div class="back__social" aria-label="Social media links">
      <span class="social-dot"></span>
      <span class="social-dot"></span>
      <span class="social-dot"></span>
    </div>
  </section>
</main>
</body>
</html>
```